Print Ad Design

I need an ad designed to promote an event that we are hosting at a trade show for placement in the show program. The art must be ready to submit to the publication by Friday, November 15th at the latest. The ad is 1/2 page in the show program that will be 4.25"X 5.5" and must be submitted as a high resolution (300dpi) PDF. Ad is full colour. The minimum bleed and trim marks are 0.25". The trade show is the Northern Herd Fair in Canada and we would like to promote a 2 day training we will be hosting at the close of the show. Our company is PastureWise Partners - Ultrasound and Diagnostics and the details that should be included in the ad are:
YOU CAN USE ULTRASOUND TO MANAGE YOUR PREG CHECKS
On Farm Ultrasound Training for Producers
When - Friday, Feb. 7th & Saturday, Feb. 8th
9 AM - 5 PM
Where - close to Herd FAIR
Lunch provided
Registration $175 per day - $300 total
Introduction to ultrasound
Reproductive system anatomy
Pregnancy diagnosis
Live on farm scanning demonstrations and practice with case discussions
Tuition redeemable towards the purchase of ultrasound system.
TO REGISTER OR LEARN MORE
email - info@pasturewisepartners.ca or call 1-800-431-5067
(I have attached our logo and some possible images to use in the ad)
Please note that the primary logo to feature is PastureWise Partners and the secondary logo to use in the ad is Veloskar Ultrasound Scanners.
THANK YOU!!!
Target Market(s)
Dairy Farmers (men and women)
Industry/Entity Type
Trade

```html
<!DOCTYPE html>
<html lang="en">
<head>
<meta charset="utf-8">
<title>On Farm Ultrasound Training for Producers</title>
<link rel="stylesheet" href="https://fonts.googleapis.com/css2?family=Arimo:wght@400;700&display=swap">
<style>
:root{
  --blue:#1b2fd6;
  --blue-deep:#0e1fa8;
  --green-1:#1d7a2c;
  --green-2:#2aa336;
  --green-3:#4cc63a;
  --green-4:#7fe02b;
  --red:#d51d12;
  --red-dark:#8f0c08;
  --title-bar:#1d1d1d;
  --orange:#f7a21b;
  --burst:#e9461d;
  --bullet:#1a1fd8;
  --white:#ffffff;
  --ink:#111111;
  --brand-blue:#1f4fa8;
}
*{margin:0;padding:0;box-sizing:border-box}
html,body{width:1200px;height:949px;overflow:hidden;background:var(--white)}
body{font-family:"Arimo",Arial,sans-serif;color:var(--ink)}
.ad{position:relative;width:1200px;height:949px;overflow:hidden;background:var(--white)}
.backdrop{position:absolute;left:0;top:0;width:1200px;height:747px}
.headline{position:absolute;left:0;top:78px;width:1200px;text-align:center;color:var(--white);font-weight:700;font-size:29px;letter-spacing:.2px}
.photo{position:absolute}
.photo-scan{left:537px;top:133px;width:663px;height:354px;background:linear-gradient(135deg,#5a4a3a 0%,#3b4a7a 35%,#d9d9d9 60%,#6b5a48 100%)}
.photo-producer{left:83px;top:487px;width:170px;height:260px;background:linear-gradient(160deg,#d6dce0 0%,#a9c7c0 45%,#3a3a3a 80%,#e8e8e8 100%)}
.event-box{position:absolute;left:83px;top:187px;width:606px;height:270px;background:linear-gradient(180deg,var(--red) 0%,var(--red-dark) 100%);border-radius:6px;box-shadow:3px 4px 6px rgba(0,0,0,.45)}
.event-title{position:absolute;left:13px;top:8px;width:580px;height:52px;background:var(--title-bar);color:var(--white);font-weight:700;font-size:21px;line-height:52px;padding-left:12px}
.event-details{position:absolute;left:18px;top:78px;color:var(--white);font-weight:700;font-size:21px;line-height:30px}
.event-details .indent{padding-left:101px}
.event-fees{position:absolute;left:6px;top:196px;width:594px;height:61px;background:var(--orange);color:var(--ink);font-weight:700;font-size:21px;line-height:27px;padding:5px 12px}
.topics{position:absolute;left:300px;top:506px;list-style:none}
.topics li{position:relative;color:var(--white);font-weight:700;font-size:25px;line-height:30px;padding-left:51px;margin-bottom:20px}
.topics li::before{content:"";position:absolute;left:0;top:6px;width:20px;height:20px;background:var(--bullet)}
.topics li:last-child{margin-top:-1px}
.badge{position:absolute;left:866px;top:496px;width:244px;height:244px}
.badge-content{position:absolute;left:866px;top:566px;width:244px;text-align:center;color:var(--white);font-weight:700}
.badge-brand{display:inline-block;background:var(--white);color:var(--burst);font-size:12px;padding:5px 8px;margin-bottom:6px}
.badge-note{font-size:11px;line-height:14px}
.brand{position:absolute;left:80px;top:800px;display:flex;align-items:center;gap:14px;color:var(--brand-blue);font-weight:700;font-size:36px}
.brand-dot{width:30px;height:30px;border-radius:50%;background:var(--brand-blue)}
.contact{position:absolute;left:529px;top:781px;color:var(--ink)}
.contact-lead{font-size:22px;line-height:28px}
.contact-line{font-weight:700;font-size:28px;line-height:36px}
</style>
</head>
<body>
<main class="ad">
  <svg class="backdrop" viewBox="0 0 1200 747" aria-hidden="true">
    <defs>
      <linearGradient id="fieldGreen" x1="0" y1="0" x2="0" y2="1">
        <stop offset="0" stop-color="#1f8a2c"/>
        <stop offset="1" stop-color="#3dbb34"/>
      </linearGradient>
    </defs>
    <rect width="1200" height="487" fill="var(--blue)"/>
    <path d="M0 150 Q300 120 560 135 L1200 135 L1200 487 L0 487 Z" fill="url(#fieldGreen)"/>
    <rect y="487" width="1200" height="70" fill="var(--green-1)"/>
    <rect y="557" width="1200" height="50" fill="var(--green-2)"/>
    <rect y="607" width="1200" height="49" fill="var(--green-3)"/>
    <rect y="656" width="1200" height="91" fill="var(--green-4)"/>
  </svg>

  <h1 class="headline">YOU CAN USE ULTRASOUND TO MANAGE YOUR PREG CHECKS!</h1>

  <div class="photo photo-scan" role="img" aria-label="Photo of technicians scanning a dairy cow with handheld ultrasound units"></div>

  <section class="event-box">
    <h2 class="event-title">On Farm Ultrasound Training for Producers</h2>
    <div class="event-details">
      <p>When:&nbsp; Friday, Feb. 7th &amp; Saturday, Feb. 8th</p>
      <p class="indent">9 AM - 5 PM</p>
      <p>Where: close to Herd FAIR</p>
    </div>
    <div class="event-fees">
      <p>Lunch provided</p>
      <p>Registration $175 per day - $300 total</p>
    </div>
  </section>

  <div class="photo photo-producer" role="img" aria-label="Photo of a producer using a portable ultrasound scanner beside a Holstein cow"></div>

  <ul class="topics">
    <li>Introduction to ultrasound</li>
    <li>Reproductive system anatomy</li>
    <li>Pregnancy diagnosis</li>
    <li>Live on farm scanning demonstrations<br>and practice with case discussions</li>
  </ul>

  <svg class="badge" viewBox="0 0 244 244" aria-hidden="true">
    <polygon fill="var(--burst)" points="122,2 133,17 147,5 154,22 171,13 174,31 192,27 191,45 209,45 204,62 221,66 212,82 228,90 216,104 230,115 215,125 227,138 210,145 219,160 201,163 206,180 188,180 189,198 172,194 168,212 152,204 144,221 130,210 122,227 114,210 100,221 92,204 76,212 72,194 55,198 56,180 38,180 43,163 25,160 34,145 17,138 29,125 14,115 28,104 16,90 32,82 23,66 40,62 35,45 53,45 52,27 70,31 73,13 90,22 97,5 111,17"/>
  </svg>
  <div class="badge-content">
    <span class="badge-brand">Veloskar Ultrasound Scanners</span>
    <p class="badge-note">Tuition redeemable<br>towards the purchase<br>of ultrasound system!</p>
  </div>

  <div class="brand">
    <span class="brand-dot"></span>
    <span class="brand-name">PastureWise Partners</span>
  </div>

  <div class="contact">
    <p class="contact-lead">To Register Or Learn More</p>
    <p class="contact-line">email: info@pasturewisepartners.ca</p>
    <p class="contact-line">or call 1-800-431-5067</p>
  </div>
</main>
</body>
</html>
```